Business card design for Automotive workshop

We need a business card for a new automotive repair and tyre shop called Ridgeback Prime Automotive located in New Zealand. We are a clean, modern and fresh workshop and company.

Front needs to feature logo,
my name:
Lachie Westergaard (director)

Address:
48 Marlow Lane
Tarawai Bay 3584

Phone: 07 842 1937
Mobile: 027 519 2764
Email: office@ridgebackmotors.co.nz
Website: ridgebackmotors.co.nz

Back needs to feature an area to write down appointment details, date and time.

Also feature a list of jobs and work we do such as,
Vehicle Servicing
All Mechanical Repairs
Warrant of Fitness
Tyres & Wheel Alignments
Automotive Diagnostics
Automotive Parts & Supplies

```html
<!DOCTYPE html>
<html lang="en">
<head>
<meta charset="utf-8">
<title>Ridgeback Prime Automotive – Business Card</title>
<link rel="stylesheet" href="https://fonts.googleapis.com/css2?family=Roboto:wght@400;500;700&display=swap">
<style>
  :root {
    --stage: #3b3b3b;
    --card-black: #1f1f20;
    --brand-red: #dc1f26;
    --ink-white: #ffffff;
    --ink-soft: #e9e9e9;
    --gloss-grey: #303032;
    --rule-grey: #bdbdbd;
  }
  * { box-sizing: border-box; margin: 0; padding: 0; }
  html, body { width: 1200px; height: 960px; overflow: hidden; }
  body {
    background: var(--stage);
    font-family: "Roboto", Arial, sans-serif;
    color: var(--ink-white);
    display: flex;
    flex-direction: column;
    align-items: center;
    justify-content: center;
    gap: 44px;
  }
  .card {
    position: relative;
    width: 720px;
    height: 411px;
    background: var(--card-black);
    border-radius: 6px;
    overflow: hidden;
    box-shadow: 0 6px 18px rgba(0,0,0,.35);
  }

  /* Back side */
  .service-list {
    position: absolute;
    list-style: none;
    font-size: 17px;
    line-height: 25px;
    color: var(--ink-soft);
  }
  .service-list li { display: flex; align-items: center; gap: 12px; }
  .service-list li::before {
    content: "";
    width: 9px; height: 9px;
    border-radius: 50%;
    background: var(--brand-red);
    flex: none;
  }
  .service-list--left { left: 48px; top: 62px; }
  .service-list--right { left: 392px; top: 62px; }
  .appointment {
    position: absolute;
    left: 48px; right: 48px; top: 166px;
  }
  .appointment__title {
    color: var(--brand-red);
    font-size: 17px;
    margin-left: 300px;
    margin-bottom: 10px;
  }
  .appointment__line {
    border-bottom: 1.5px dashed var(--rule-grey);
    height: 34px;
  }
  .back-wordmark {
    position: absolute;
    right: 48px; bottom: 34px;
    font-size: 34px;
    font-weight: 700;
    letter-spacing: 2px;
    text-transform: uppercase;
    color: var(--gloss-grey);
    white-space: nowrap;
  }

  /* Front side */
  .front-wordmark {
    position: absolute;
    right: 44px; top: 62px;
    display: flex;
    align-items: center;
    gap: 14px;
    font-size: 34px;
    font-weight: 700;
    letter-spacing: 2px;
    text-transform: uppercase;
    color: var(--ink-white);
    white-space: nowrap;
  }
  .front-wordmark__mark {
    width: 20px; height: 20px;
    background: var(--brand-red);
    flex: none;
  }
  .contact-band {
    position: absolute;
    left: 0; right: 0; bottom: 0;
    height: 215px;
    background: var(--brand-red);
    display: flex;
    align-items: center;
    padding: 0 40px 0 0;
  }
  .person {
    width: 360px;
    text-align: right;
    padding-right: 22px;
    font-size: 20px;
    line-height: 26px;
  }
  .person__name { font-size: 28px; font-weight: 700; line-height: 36px; }
  .band-divider {
    width: 2px;
    height: 140px;
    background: var(--card-black);
  }
  .contact-list {
    list-style: none;
    padding-left: 22px;
    font-size: 19px;
    line-height: 33px;
  }
  .contact-list li { display: flex; align-items: center; gap: 12px; white-space: nowrap; }
  .contact-list svg { width: 18px; height: 18px; flex: none; }
</style>
</head>
<body>

  <section class="card card--back" aria-label="Card back">
    <ul class="service-list service-list--left">
      <li>Vehicle Servicing</li>
      <li>All Mechanical Repairs</li>
      <li>Warrant of Fitness</li>
    </ul>
    <ul class="service-list service-list--right">
      <li>Tyres &amp; Wheel Alignments</li>
      <li>Automotive Diagnostics</li>
      <li>Automotive Parts &amp; Supplies</li>
    </ul>
    <div class="appointment">
      <p class="appointment__title">Appointment Details:</p>
      <div class="appointment__line"></div>
      <div class="appointment__line"></div>
      <div class="appointment__line"></div>
    </div>
    <p class="back-wordmark">Ridgeback Prime Automotive</p>
  </section>

  <section class="card card--front" aria-label="Card front">
    <div class="front-wordmark">
      <span class="front-wordmark__mark"></span>
      <span>Ridgeback Prime Automotive</span>
    </div>
    <div class="contact-band">
      <div class="person">
        <p class="person__name">Lachie Westergaard</p>
        <p>Director</p>
        <p>48 Marlow Lane</p>
        <p>Tarawai Bay 3584</p>
      </div>
      <div class="band-divider"></div>
      <ul class="contact-list">
        <li>
          <svg viewBox="0 0 18 18" aria-hidden="true"><rect x="4" y="1" width="10" height="16" rx="2" fill="none" stroke="#fff" stroke-width="1.8"/><circle cx="9" cy="14" r="1" fill="#fff"/></svg>
          027 519 2764
        </li>
        <li>
          <svg viewBox="0 0 18 18" aria-hidden="true"><path d="M4 1.5l3 3.2-1.8 2a10 10 0 0 0 6 6l2-1.8 3.3 3-2 2.3C8 15.6 2.3 10 1.7 3.5z" fill="#fff"/></svg>
          07 842 1937
        </li>
        <li>
          <svg viewBox="0 0 18 18" aria-hidden="true"><rect x="1" y="4" width="16" height="11" fill="#fff"/><path d="M1 4l8 6 8-6" fill="none" stroke="#dc1f26" stroke-width="1.5"/></svg>
          office@ridgebackmotors.co.nz
        </li>
        <li>
          <svg viewBox="0 0 18 18" aria-hidden="true"><circle cx="9" cy="9" r="7.5" fill="none" stroke="#fff" stroke-width="1.8"/><ellipse cx="9" cy="9" rx="3.2" ry="7.5" fill="none" stroke="#fff" stroke-width="1.4"/><path d="M1.5 9h15" stroke="#fff" stroke-width="1.4"/></svg>
          www.ridgebackmotors.co.nz
        </li>
      </ul>
    </div>
  </section>

</body>
</html>
```